Online Training company needs a new website design (Wordpress)

We are looking for a new design for our website (run on WordPress). We currently have two websites (quizharbor.net) and (velmarlearning.net) and are trying to combine them into a single design.

The site should contain the following sections (Start Here, courses, labs, practice exams, exam vouchers, books, articles, about us).

Start Here - With so many options on our site, we think it would be a good idea to have this page that will allow us to give students an overview of our different products/services and where to start when they first find out about our company.

Courses - These are our online video courses (products), currently hosted at velmarlearning.net. Each course has its own "product page".

Labs - These are online lab environments that a student can purchase. The layout for these would be similar to a course, but the purchase option will be different (our web developer will code all the back end stuff to make it work).

Practice Exams - This will allow students to take practice questions to study for their exams.

Exam Vouchers - Students can purchase their exam vouchers here at a discounted price for their certification exams.

Books - Will link to a page that displays our books that are available on Tarvix. (Examples of the covers are attached so you can see our current designs.)

Articles - This will be our "blog" area for us to post articles each week.

About Us - A short about us page describing our company.

***
As for the design of the page itself, we like the current color scheme at velmarlearning.net, but the layout isn't working well. It was fine when we just had video courses, but as we have added new products it is becoming more and more cumbersome.

I have been looking for inspiration around the web, and saw brightfallowearnings.net as a good example of trying to provide focus to new users, while breaking out various parts of a business that contains 4-6 different product lines/topics. Another example of a site we like is clipacademyweb.net.

That said, we aren't looking to simply copy either site, and are completely open to recommendations and designs you may have.

Thank you and we look forward to working with you!

```html
<!DOCTYPE html>
<html lang="en">
<head>
<meta charset="utf-8">
<title>OpsITv3 Certification: Quiz Harbor</title>
<link href="https://fonts.googleapis.com/css2?family=Lato:wght@300;400;700&display=swap" rel="stylesheet">
<style>
:root{
  --ink:#1f2430;
  --muted:#5a5f6b;
  --faint:#b5b8c0;
  --frame:#3a3f7a;
  --brand-blue:#2a44c9;
  --sky-a:#3ad6f6;
  --sky-b:#3b7ed2;
  --violet-a:#3b5fb8;
  --violet-b:#8a55c6;
  --accent-yellow:#f2b51c;
  --placeholder:#d4d4d6;
  --white:#ffffff;
}
*{box-sizing:border-box;margin:0;padding:0}
html,body{width:1200px;height:1200px;overflow:hidden;background:var(--white)}
body{font-family:'Lato',sans-serif;color:var(--ink)}
.stage{position:absolute;left:0;top:0;width:1500px;height:1500px;transform:scale(.8);transform-origin:0 0}
.page{position:absolute;left:548px;top:0;width:424px;height:1500px;border-left:2px solid var(--frame);border-right:2px solid var(--frame);background:var(--white)}
.abs{position:absolute}
/* hero */
.hero{left:0;top:0;width:420px;height:218px;background:linear-gradient(120deg,#2b2f36 0%,#15181d 45%,#263544 70%,#101317 100%)}
.nav{left:0;top:0;width:420px;height:26px;background:rgba(255,255,255,.06)}
.logo{left:30px;top:9px;font-size:5px;font-weight:700;color:var(--white);letter-spacing:.3px}
.menu{left:150px;top:10px;display:flex;gap:7px;font-size:4.6px;color:#e6e8ee}
.search{left:400px;top:8px}
.hero-title{left:30px;top:70px;font-size:18.5px;font-weight:400;color:var(--white);white-space:nowrap}
.hero-sub{left:30px;top:96px;font-size:12px;font-weight:400;color:var(--white);white-space:nowrap}
.hero-copy{left:30px;top:117px;width:225px;font-size:5.6px;line-height:8px;color:#d6d9e0}
.btn-primary{background:var(--brand-blue);color:var(--white);font-size:4.6px;font-weight:700;display:flex;align-items:center;justify-content:center}
.hero-cta{left:30px;top:180px;width:92px;height:12px;border-radius:1px}
/* advantage */
.section-title{font-size:10.5px;font-weight:700;color:var(--ink);white-space:nowrap}
.feature-icon{width:14px;height:14px}
.feature-title{font-size:8.8px;font-weight:400;color:var(--ink);white-space:nowrap}
.feature-copy{font-size:5.6px;line-height:8px;color:var(--muted)}
/* courses */
.courses{left:0;top:703px;width:420px;height:211px;background:linear-gradient(35deg,var(--sky-a) 0%,#3ab5ea 50%,var(--sky-b) 100%)}
.courses-title{left:30px;top:14px;font-size:10px;font-weight:400;color:var(--white)}
.card{width:106px;height:131px;background:var(--white);border:1px solid #c9d6ea;top:34px}
.card-art{left:3px;top:3px;width:98px;height:55px;border:1px solid #2c3a7a;background:linear-gradient(135deg,#4a5f9a,#8a9cc9 50%,#3e5a6e)}
.card-art .label{position:absolute;left:0;width:98px;top:30px;font-size:9px;line-height:9px;color:var(--white);text-align:center}
.price{left:3px;top:60px;font-size:3.6px;font-weight:700;color:var(--ink)}
.card-name{left:3px;top:64px;width:100px;font-size:6.6px;font-weight:400;color:var(--ink);white-space:nowrap;overflow:hidden}
.card-copy{left:3px;top:78px;width:92px;font-size:4.3px;line-height:7.5px;color:var(--faint)}
.card-buy{left:3px;top:114px;width:48px;height:13px;font-size:4px}
.card-more{left:53px;top:114px;width:48px;height:13px;border:1px solid var(--brand-blue);color:var(--brand-blue);font-size:4px;display:flex;align-items:center;justify-content:center}
.explore{left:174px;top:188px;width:73px;height:13px;background:var(--white);border:1px solid var(--brand-blue);color:var(--brand-blue);font-size:4.2px;display:flex;align-items:center;justify-content:center;gap:4px}
/* learn */
.learn-rule{left:30px;top:943px;width:134px;height:1px;background:var(--accent-yellow)}
.mode-box{top:993px;width:74px;height:53px;background:var(--placeholder)}
.mode-copy{top:1060px;width:86px;font-size:4.6px;line-height:7px;color:var(--muted);text-align:center}
/* insider */
.insider{left:0;top:1129px;width:420px;height:102px;background:linear-gradient(90deg,var(--violet-a),var(--violet-b))}
.insider-title{left:0;width:420px;top:12px;text-align:center;font-size:9px;font-weight:400;letter-spacing:1.2px;color:var(--white)}
.insider-copy{left:60px;width:300px;top:28px;text-align:center;font-size:5.5px;line-height:8px;color:#e7e3f6}
.email{left:121px;top:53px;width:182px;height:17px;background:var(--white);border:1px solid #d5d0ea;font-size:4.8px;color:#9a9aa6;display:flex;align-items:center;padding-left:5px}
.email svg{position:absolute;right:5px;top:4px}
.fine{left:60px;width:300px;top:76px;text-align:center;font-size:3.4px;line-height:8px;font-style:italic;color:#dcd6f2}
/* featured */
.featured-label{left:30px;top:1287px;font-size:5px;color:var(--muted)}
.brand{top:1285px;font-size:7px;font-weight:700;color:var(--ink);white-space:nowrap}
</style>
</head>
<body>
<div class="stage">
<main class="page">

  <header class="abs hero" role="img" aria-label="Dark photo of a laptop showing lines of code">
    <div class="abs nav"></div>
    <div class="abs logo">LOGO</div>
    <nav class="abs menu"><span>Start Here</span><span>Courses</span><span>Labs</span><span>Practice Exams</span><span>Exam Vouchers</span><span>Books</span><span>Articles</span><span>About Us</span></nav>
    <svg class="abs search" width="9" height="9" viewBox="0 0 9 9"><circle cx="3.8" cy="3.8" r="2.8" fill="none" stroke="#fff" stroke-width=".8"/><line x1="5.8" y1="5.8" x2="8.3" y2="8.3" stroke="#fff" stroke-width=".8"/></svg>
    <h1 class="abs hero-title">OpsITv3 Certification: Quiz Harbor</h1>
    <p class="abs hero-sub">Learn the information. Pass the certification.</p>
    <p class="abs hero-copy">Do you want to get OpsITv3 Foundations certified quickly?<br>If so, you have come to the right place. We can help you study the material quickly and get certified in no time at all. Using our online videos, textbooks, or quiz application, we have numerous ways to ensure you get certified in the shortest time possible, with Quiz Harbor.</p>
    <a class="abs btn-primary hero-cta">Get Your Free eBook Today</a>
  </header>

  <h2 class="abs section-title" style="left:31px;top:232px">THE QUIZ HARBOR ADVANTAGE</h2>

  <svg class="abs feature-icon" style="left:32px;top:282px" viewBox="0 0 14 14"><circle cx="7" cy="7" r="6.5" fill="#fff" stroke="#e2e2e2" stroke-width=".6"/><circle cx="7" cy="6" r="2.6" fill="var(--accent-yellow)"/><rect x="5.8" y="8.4" width="2.4" height="2" fill="#c48a10"/></svg>
  <h3 class="abs feature-title" style="left:30px;top:299px">Learn Faster and Get Certified</h3>
  <p class="abs feature-copy" style="left:30px;top:315px;width:200px">Due to the design of our materials, you will learn faster and focus your studies on passing your certifications. With our tools and techniques, you will be ready to take and pass your certification exam on your first attempt!</p>
  <div class="abs" style="left:249px;top:285px;width:121px;height:65px;background:linear-gradient(180deg,#8fb0cf,#dfe7ef 70%,#b9c9d8)" role="img" aria-label="Photo of a ladder reaching up into the clouds"></div>

  <div class="abs" style="left:30px;top:387px;width:121px;height:65px;background:linear-gradient(120deg,#2e2a33,#5b4a4e 50%,#6a7aa8)" role="img" aria-label="Photo of a team working on laptops at a table"></div>
  <svg class="abs feature-icon" style="left:176px;top:388px" viewBox="0 0 14 14"><circle cx="7" cy="7" r="6.5" fill="#fff" stroke="#e2e2e2" stroke-width=".6"/><path d="M4 10 L10 4" stroke="var(--accent-yellow)" stroke-width="1.8" stroke-linecap="round"/></svg>
  <h3 class="abs feature-title" style="left:174px;top:405px">Unlimited Access and Support</h3>
  <p class="abs feature-copy" style="left:174px;top:421px;width:200px">With our monthly membership plan, you receive unlimited access to all of our video courses and email support for just $9/month. With our premium plan, you will also gain exclusive access to our live "office hours" sessions where you can gain answers in real time.</p>

  <svg class="abs feature-icon" style="left:32px;top:487px" viewBox="0 0 14 14"><circle cx="7" cy="7" r="6.5" fill="#fff" stroke="#e2e2e2" stroke-width=".6"/><path d="M7 3.5 L10 4.8 V7.5 C10 9.3 8.6 10.5 7 11 C5.4 10.5 4 9.3 4 7.5 V4.8 Z" fill="none" stroke="var(--accent-yellow)" stroke-width=".9"/></svg>
  <h3 class="abs feature-title" style="left:30px;top:504px">Training the Cybersecurity Workforce</h3>
  <p class="abs feature-copy" style="left:30px;top:521px;width:195px">We strive to train the cybersecurity workforce of today and tomorrow. Whether you need to earn your next certification to be competitive for that position, or you just need to do your continuing education to maintain your current certifications, Velmar Learning is here to support you.</p>
  <div class="abs" style="left:249px;top:486px;width:121px;height:75px;background:linear-gradient(135deg,#1d2a27,#2f4440 60%,#5b7c86)" role="img" aria-label="Photo of a person at a computer screen in a dark room"></div>

  <div class="abs" style="left:30px;top:600px;width:117px;height:57px;background:linear-gradient(180deg,#2f4a4e,#1f2f33 70%,#3a3d40)" role="img" aria-label="Photo of a person relaxing at a desk with a laptop"></div>
  <svg class="abs feature-icon" style="left:173px;top:602px" viewBox="0 0 14 14"><circle cx="7" cy="7" r="6.5" fill="#fff" stroke="#e2e2e2" stroke-width=".6"/><path d="M4 7.2 L6.2 9.4 L10.2 4.6" fill="none" stroke="var(--accent-yellow)" stroke-width="1.2" stroke-linecap="round"/></svg>
  <h3 class="abs feature-title" style="left:171px;top:618px">Satisfaction Guaranteed</h3>
  <p class="abs feature-copy" style="left:171px;top:634px;width:200px">With our unconditional satisfaction guarantee,you have nothing to worry about. Become a member or choose an individual course today. We have a 30-day money-back guarantee on all of our courses.</p>

  <section class="abs courses">
    <h2 class="abs courses-title">Our Courses:</h2>

    <article class="abs card" style="left:31px">
      <div class="abs card-art" role="img" aria-label="Collage of course artwork with plain certification badges"><span class="label">Full<br>Access</span></div>
      <div class="abs price">$9 / month</div>
      <h3 class="abs card-name">Full access to all our courses.</h3>
      <p class="abs card-copy">With our $9/m plan, you get unlimited access to all our courses!</p>
      <a class="abs btn-primary card-buy">Buy This Course</a>
      <a class="abs card-more">Learn More...</a>
    </article>

    <article class="abs card" style="left:158px">
      <div class="abs card-art" role="img" aria-label="Collage of course artwork with plain certification badges"><span class="label">Full<br>Access</span></div>
      <div class="abs price">$299</div>
      <h3 class="abs card-name">OpsIT Foundation (Exam Voucher)</h3>
      <p class="abs card-copy">Purchase your discounted OpsIT Foundation exam voucher directly from Velmar Learning.</p>
      <a class="abs btn-primary card-buy">Buy This Course</a>
      <a class="abs card-more">Learn More...</a>
    </article>

    <article class="abs card" style="left:285px">
      <div class="abs card-art" role="img" aria-label="Collage of course artwork with plain certification badges"><span class="label">Full<br>Access</span></div>
      <div class="abs price">$299</div>
      <h3 class="abs card-name">ProjectPath Foundation</h3>
      <p class="abs card-copy">Purchase your discounted ProjectPath Foundation exam voucher directly from Velmar Learning.</p>
      <a class="abs btn-primary card-buy">Buy This Course</a>
      <a class="abs card-more">Learn More...</a>
    </article>

    <a class="abs explore">Explore other courses <svg width="4" height="5" viewBox="0 0 4 5"><path d="M1 .5 L3 2.5 L1 4.5" fill="none" stroke="var(--brand-blue)" stroke-width=".7"/></svg></a>
  </section>

  <h2 class="abs section-title" style="left:30px;top:930px">How you can learn with us:</h2>
  <div class="abs learn-rule"></div>

  <svg class="abs" style="left:57px;top:970px" width="18" height="14" viewBox="0 0 18 14"><rect x="1" y="1" width="16" height="10" rx="1" fill="none" stroke="var(--brand-blue)" stroke-width="1.2"/><path d="M7.5 3.5 L11 6 L7.5 8.5 Z" fill="var(--brand-blue)"/><line x1="0" y1="13" x2="18" y2="13" stroke="var(--brand-blue)" stroke-width="1.2"/></svg>
  <svg class="abs" style="left:154px;top:969px" width="12" height="15" viewBox="0 0 12 15"><rect x="1" y="1" width="10" height="13" fill="none" stroke="var(--brand-blue)" stroke-width=".8"/><line x1="3" y1="1" x2="3" y2="14" stroke="var(--brand-blue)" stroke-width=".8"/></svg>
  <svg class="abs" style="left:246px;top:969px" width="9" height="15" viewBox="0 0 9 15"><rect x="1" y="1" width="7" height="13" rx="1" fill="none" stroke="var(--brand-blue)" stroke-width=".9"/><circle cx="4.5" cy="12" r=".7" fill="var(--brand-blue)"/></svg>
  <svg class="abs" style="left:339px;top:970px" width="20" height="14" viewBox="0 0 20 14"><path d="M1 5 L10 1 L19 5 L10 9 Z" fill="none" stroke="var(--brand-blue)" stroke-width=".8"/><path d="M5 7 V11 C7 13 13 13 15 11 V7" fill="none" stroke="var(--brand-blue)" stroke-width=".8"/><line x1="18" y1="5" x2="18" y2="10" stroke="var(--brand-blue)" stroke-width=".8"/></svg>

  <div class="abs mode-box" style="left:29px" role="img" aria-label="Video course preview"></div>
  <div class="abs mode-box" style="left:122px" role="img" aria-label="Book series preview"></div>
  <div class="abs mode-box" style="left:214px" role="img" aria-label="Quiz app preview"></div>
  <div class="abs mode-box" style="left:312px" role="img" aria-label="Articles blog preview"></div>

  <p class="abs mode-copy" style="left:23px">Using our Quiz Harbor video series, we take complicated certification exams and teach you to pass within a few hours.</p>
  <p class="abs mode-copy" style="left:116px">Our Quiz Harbor book series will get you certified in the shortest amount of time. Learn what you need to get certified today!</p>
  <p class="abs mode-copy" style="left:208px">Our quiz apps prepare you for the certification exam while on the go. Each question comes with a complete explanation.</p>
  <p class="abs mode-copy" style="left:306px">Signup for your daily dose of training with our constantly updated blog feed of new content to learn quickly.</p>

  <section class="abs insider">
    <h2 class="abs insider-title">BECOME A QUIZ HARBOR INSIDER</h2>
    <p class="abs insider-copy">Join thousands of students who recieved our free eBook of OpsITv3 Foundation (Quiz Harbor) and an exclusive discount on our video course.</p>
    <label class="abs email">Enter e-mail address
      <svg width="12" height="9" viewBox="0 0 12 9"><rect x=".5" y=".5" width="11" height="8" fill="none" stroke="var(--violet-a)" stroke-width=".8"/><path d="M.5 .5 L6 5 L11.5 .5" fill="none" stroke="var(--violet-a)" stroke-width=".8"/></svg>
    </label>
    <p class="abs fine">By subscribing to Quiz Harbor Insider, you will receive a free eBook sample version of the<br>OpsITv3 Foundations book with over 50 pages of excellent content including a free full practice test</p>
  </section>

  <span class="abs featured-label">As featured on:</span>
  <span class="abs brand" style="left:98px">Lernova</span>
  <span class="abs brand" style="left:168px">Tarvix</span>
  <span class="abs brand" style="left:236px">Vidora</span>
  <span class="abs brand" style="left:304px">Brookline Study</span>

</main>
</div>
</body>
</html>
```